Norvale Telecom Twitter Background

We want to use our existing logo and colours and develop a background for our LinkedIn page and also Twitter page.
Updates

Project Deadline Extended
Reason: Due to very low level of designs submitted I am extending project deadline. Thank you to all who have submitted designs so far.

Industry/Entity Type

Telecom

Requirements
Must have
• Add the company tagline to project
• keeping you connected
• or
• Keeping You Connected
Nice to have
• Fiber optic design element
• In-Building DAS antenna design element
• Ethernet CAT5 design element
• WiFi element

```html
<!DOCTYPE html>
<html lang="en">
<head>
<meta charset="utf-8">
<title>Norvale Telecom – Social Banner</title>
<link rel="stylesheet" href="https://fonts.googleapis.com/css2?family=Source+Sans+3:wght@400;600&display=swap">
<style>
  :root {
    --page-bg: #e4e4e4;
    --mesh-light: #2e2e2e;
    --mesh-dark: #0e0e0e;
    --signal-red: #e01b1b;
    --frame-red: #c8141a;
    --text-white: #ffffff;
  }
  * { margin: 0; padding: 0; box-sizing: border-box; }
  html, body {
    width: 1200px;
    height: 1000px;
    overflow: hidden;
    background: var(--page-bg);
  }
  .canvas {
    position: relative;
    width: 1200px;
    height: 1000px;
  }
  .banner {
    position: absolute;
    left: 40px;
    top: 314px;
    width: 1118px;
    height: 372px;
    overflow: hidden;
    box-shadow: 0 6px 18px rgba(0,0,0,0.35);
  }
  .mesh-texture {
    position: absolute;
    inset: 0;
    background: radial-gradient(ellipse at 50% 45%, var(--mesh-light) 0%, #1c1c1c 55%, var(--mesh-dark) 100%);
  }
  .broadcast-icon {
    position: absolute;
    left: 84px;
    top: 140px;
    width: 162px;
    height: 88px;
  }
  .brand-frame {
    position: absolute;
    left: 318px;
    top: 102px;
    width: 459px;
    height: 155px;
    border: 1.5px solid var(--frame-red);
    border-radius: 9px;
    display: flex;
    align-items: center;
    justify-content: center;
    gap: 14px;
  }
  .brand-dot {
    width: 18px;
    height: 18px;
    border-radius: 50%;
    background: var(--signal-red);
  }
  .brand-name {
    font-family: "Source Sans 3", sans-serif;
    font-weight: 600;
    font-size: 50px;
    color: var(--text-white);
    letter-spacing: 0.5px;
  }
  .tower-illustration {
    position: absolute;
    left: 845px;
    top: 118px;
    width: 108px;
    height: 130px;
    border-radius: 4px;
    background: linear-gradient(180deg, #8a8a8a 0%, #b33030 55%, var(--signal-red) 100%);
  }
  .tagline {
    position: absolute;
    left: 808px;
    top: 318px;
    font-family: "Source Sans 3", sans-serif;
    font-weight: 400;
    font-size: 22px;
    color: var(--text-white);
    white-space: nowrap;
  }
  .tagline-accent { color: var(--signal-red); }
</style>
</head>
<body>
<div class="canvas">
  <section class="banner">
    <div class="mesh-texture" role="img" aria-label="Dark hexagonal mesh texture background"></div>

    <svg class="broadcast-icon" viewBox="0 0 162 88" aria-hidden="true">
      <g fill="none" stroke="var(--signal-red)">
        <path d="M20 6 A55 55 0 0 0 20 82" stroke-width="10"/>
        <path d="M142 6 A55 55 0 0 1 142 82" stroke-width="10"/>
        <path d="M44 20 A36 36 0 0 0 44 68" stroke-width="8"/>
        <path d="M118 20 A36 36 0 0 1 118 68" stroke-width="8"/>
        <path d="M64 32 A18 18 0 0 0 64 56" stroke-width="6"/>
        <path d="M98 32 A18 18 0 0 1 98 56" stroke-width="6"/>
      </g>
      <circle cx="81" cy="44" r="6" fill="var(--signal-red)"/>
    </svg>

    <div class="brand-frame">
      <span class="brand-dot" aria-hidden="true"></span>
      <span class="brand-name">Norvale Telecom</span>
    </div>

    <div class="tower-illustration" role="img" aria-label="Illustration of a red and white antenna tower sending signal waves"></div>

    <p class="tagline"><span class="tagline-accent">Keeping</span> You Connected</p>
  </section>
</div>
</body>
</html>
```